Automotive Locksmiith company needs a website design and mobile website

We need a website design and a mobile design for an automotive locksmith company called Cedarline Autoworks LLC.We are based in the center of the Dallas-Fort Worth Metroplex. We have a website that was directed more towards the towing services we also offer. We would like to have it more towards our locksmith products. Our main services include:
Auto keys duplication
Cutting of new car keys
Car Lockouts
Laser key replacement
Cutting keys by code
Broken key extractions
Production of transponder keys
Key fob programming
Door lock repairs
Ignition repairs/replacement
We work on 95% of the automotive market that includes Vorra, Belvo, KTZ, Merrowind, Tanquelle, Polgrave, Brunt, QR, Solvane, Pirel, Zoravelo, Uto, Harwick, Quorel, Telvar, Ostravin, Fendale, Pavo, Rulko Kelvarona , Brisel, Varuno, Drexmotor, Tesko.
We are one of the most affordable services in the DFW area . Our prices for transponder copies start at $35 per key. We provide services for high-end vehicles also as KTZ and Ostravin. We can program the new proximity keys for Telvar Vehicles 2013-up. We also work on the new Pell Vehicles 20-13 and up including the Pell Caravel head remote key.
We would like to have a similar style to the website we already have with the option to schedule an appointment on the mobile website. This mobile application will deliver an email when a new customer is requiring the service. It will ask for Year, Make, Model , Service to be performed( Key copy, Lockout, Lost Key, Change Ignition lock, change door lock, Other services.) Description of the service to be performed, Address, Select time of service.
Our current website is cedarlineautoworks.example

Reason: Need pictures of webpages inside design (about us , location etc) and mobile pictures( how website looks in zelPad / norvix)

Automotive

• check word attachment

```html
<!DOCTYPE html>
<html lang="en">
<head>
<meta charset="utf-8">
<title>Cedarline Autoworks LLC – Mobile About &amp; Services</title>
<link href="https://fonts.googleapis.com/css2?family=Covered+By+Your+Grace&family=Roboto:wght@300;400&display=swap" rel="stylesheet">
<style>
  :root {
    --backdrop: #e9ece8;
    --page: #ffffff;
    --ink: #1a1a1a;
    --body-text: #444444;
    --label-text: #6b6b6b;
    --rule: #dcdcdc;
    --navy: #1f3f72;
    --navy-ring: #c9ced6;
    --glyph: #ffffff;
    --photo-blue: #2b4c9a;
    --photo-light: #e8edf3;
  }
  * { box-sizing: border-box; margin: 0; padding: 0; }
  html, body { width: 1200px; height: 1200px; overflow: hidden; }
  body {
    background: var(--backdrop);
    display: flex;
    justify-content: center;
    align-items: center;
    font-family: "Roboto", Arial, sans-serif;
  }
  .mobile-page {
    width: 640px;
    height: 1136px;
    background: var(--page);
    padding: 34px 40px 0;
    overflow: hidden;
  }
  .section-heading {
    display: flex;
    align-items: center;
    gap: 16px;
  }
  .section-heading h2 {
    font-family: "Covered By Your Grace", cursive;
    font-weight: 400;
    font-size: 44px;
    color: var(--ink);
    line-height: 1;
    white-space: nowrap;
  }
  .heading-rule {
    flex: 1;
    height: 10px;
    background: var(--rule);
  }
  .about-photo {
    margin-top: 16px;
    height: 250px;
    background: linear-gradient(100deg, var(--photo-blue) 0%, var(--photo-blue) 38%, #9aa9c2 50%, var(--photo-light) 70%, #f6f7f9 100%);
  }
  .about-text {
    margin-top: 18px;
    font-size: 14px;
    font-weight: 300;
    line-height: 1.45;
    color: var(--body-text);
  }
  .section-divider {
    margin: 16px 0 22px;
    height: 10px;
    background: var(--rule);
  }
  .services-grid {
    margin-top: 26px;
    display: grid;
    grid-template-columns: repeat(3, 1fr);
    row-gap: 30px;
    text-align: center;
  }
  .service-item { display: flex; flex-direction: column; align-items: center; }
  .service-icon {
    width: 108px;
    height: 108px;
    border-radius: 50%;
    background: var(--navy);
    border: 4px solid var(--navy-ring);
    display: flex;
    align-items: center;
    justify-content: center;
  }
  .service-icon svg { width: 58px; height: 58px; }
  .service-label {
    margin-top: 10px;
    font-size: 14px;
    font-weight: 300;
    color: var(--label-text);
    line-height: 1.25;
    width: 130px;
  }
</style>
</head>
<body>
  <main class="mobile-page">
    <section class="about-section">
      <div class="section-heading">
        <h2>About Us</h2>
        <span class="heading-rule"></span>
      </div>
      <div class="about-photo" role="img" aria-label="Photo of a mechanic in blue overalls holding a wrench in a bright workshop"></div>
      <p class="about-text">We are a locally owned company with over 6 years of experience in the automotive industry. We provide towing and automotive locksmith services to the Dallas Ft-Worth Area. Our main goal is to provide unmatched customer service both to the client and your customer. You will appreciate the value of our professional approach to all your automotive needs. Our experienced staff will always be eager to assist you. We look forward to being your reliable business partner when your locksmith needs arise. Our business relationships with clients are warm, friendly and sincere. Our valued clients count on us to deliver excellent service and we're obliged to deliver above and beyond! We want every interaction you have with Cedarline Autoworks LLC to be refreshing and delightful; especially given the circumstances that brought you to us! We eliminate stress or incident.</p>
      <div class="section-divider"></div>
    </section>

    <section class="services-section">
      <div class="section-heading">
        <h2>Services</h2>
        <span class="heading-rule"></span>
      </div>
      <div class="services-grid">
        <div class="service-item">
          <div class="service-icon">
            <svg viewBox="0 0 60 60" fill="var(--glyph)"><circle cx="16" cy="10" r="5" fill="none" stroke="var(--glyph)" stroke-width="3"/><rect x="20" y="8.5" width="22" height="3"/><rect x="36" y="11" width="3" height="5"/><path d="M12 30 L17 20 H43 L48 30 H52 V46 H46 V51 H40 V46 H20 V51 H14 V46 H8 V30 Z M18 30 H42 L39 24 H21 Z"/></svg>
          </div>
          <p class="service-label">Cutting of new car keys</p>
        </div>
        <div class="service-item">
          <div class="service-icon">
            <svg viewBox="0 0 60 60" fill="var(--glyph)"><rect x="8" y="18" width="28" height="24" rx="5"/><rect x="34" y="27" width="20" height="6"/><rect x="44" y="33" width="3" height="6"/><rect x="50" y="33" width="3" height="5"/><rect x="16" y="24" width="12" height="10" rx="1" fill="var(--navy)"/><path d="M18 24 V20 a4 4 0 0 1 8 0 V24" fill="none" stroke="var(--navy)" stroke-width="2.5"/></svg>
          </div>
          <p class="service-label">Car Lockouts</p>
        </div>
        <div class="service-item">
          <div class="service-icon">
            <svg viewBox="0 0 60 60" fill="var(--glyph)"><path d="M8 40 L13 30 H35 L40 40 H43 V52 H5 V40 Z M14 40 H34 L32 34 H16 Z"/><path d="M36 26 C40 20 44 22 44 16" fill="none" stroke="var(--glyph)" stroke-width="3"/><rect x="40" y="6" width="10" height="10" rx="2"/><rect x="42" y="2" width="2" height="5"/><rect x="46" y="2" width="2" height="5"/></svg>
          </div>
          <p class="service-label">Laser key replacement</p>
        </div>
        <div class="service-item">
          <div class="service-icon">
            <svg viewBox="0 0 60 60" fill="var(--glyph)"><circle cx="16" cy="20" r="8"/><path d="M4 48 V40 a12 10 0 0 1 24 0 V48 Z"/><rect x="26" y="14" width="20" height="18" rx="2"/><circle cx="36" cy="23" r="4" fill="var(--navy)"/><circle cx="48" cy="12" r="6" fill="none" stroke="var(--glyph)" stroke-width="3"/><rect x="22" y="44" width="34" height="4"/></svg>
          </div>
          <p class="service-label">Cutting keys by code</p>
        </div>
        <div class="service-item">
          <div class="service-icon">
            <svg viewBox="0 0 60 60" fill="none" stroke="var(--glyph)" stroke-width="4" stroke-linejoin="round"><path d="M26 14 H10 V48 H44 V34"/><path d="M20 38 C22 26 30 20 42 20"/><path d="M36 12 L46 20 L36 28" fill="var(--glyph)"/></svg>
          </div>
          <p class="service-label">Broken key extractions</p>
        </div>
        <div class="service-item">
          <div class="service-icon">
            <svg viewBox="0 0 60 60" fill="var(--glyph)"><path d="M10 14 H28 L34 24 V46 H28 V40 H12 V46 H6 V24 Z M12 24 H28 L25 18 H15 Z"/><circle cx="38" cy="32" r="7"/><rect x="42" y="34" width="14" height="4" transform="rotate(35 42 34)"/></svg>
          </div>
          <p class="service-label">Production of transponder keys</p>
        </div>
        <div class="service-item">
          <div class="service-icon">
            <svg viewBox="0 0 60 60" fill="var(--glyph)"><rect x="16" y="16" width="28" height="28" rx="3"/><rect x="23" y="23" width="14" height="14" fill="var(--navy)"/><g stroke="var(--glyph)" stroke-width="2"><path d="M20 8v6M26 8v6M32 8v6M38 8v6M20 46v6M26 46v6M32 46v6M38 46v6M8 20h6M8 26h6M8 32h6M8 38h6M46 20h6M46 26h6M46 32h6M46 38h6"/></g></svg>
          </div>
          <p class="service-label">Key fob programming</p>
        </div>
        <div class="service-item">
          <div class="service-icon">
            <svg viewBox="0 0 60 60" fill="var(--glyph)"><path d="M8 32 L15 20 H45 L52 32 H55 V46 H49 V50 H43 V46 H17 V50 H11 V46 H5 V32 Z M16 32 H44 L40 25 H20 Z"/><circle cx="14" cy="39" r="3" fill="var(--navy)"/><circle cx="46" cy="39" r="3" fill="var(--navy)"/><rect x="4" y="12" width="10" height="8" rx="1"/></svg>
          </div>
          <p class="service-label">Door lock repairs</p>
        </div>
        <div class="service-item">
          <div class="service-icon">
            <svg viewBox="0 0 60 60" fill="none" stroke="var(--glyph)" stroke-width="5" stroke-linecap="round"><path d="M20 16 A18 18 0 1 0 40 16"/><path d="M30 8 V30"/></svg>
          </div>
          <p class="service-label">Ignition repairs</p>
        </div>
      </div>
    </section>
  </main>
</body>
</html>
```